The bright window tour 2019

I need an improvement of my own design for a speaking tour on shame and mental health. The advertisement will be for social media. I would like someone to remove the background and do something creative and contemporary. My preference is just my head and shoulders.

Target Market(s)

Church pastors and leaders of mental health organisations

Industry/Entity Type

Mental Health

Requirements
Must have
• The same wording as original
• Delete background and replace with something that is simple but funky

```html
<!DOCTYPE html>
<html lang="en">
<head>
<meta charset="utf-8">
<title>The Bright Window Tour 2019</title>
<link href="https://fonts.googleapis.com/css2?family=Poppins:wght@400;700&display=swap" rel="stylesheet">
<style>
  :root {
    --purple: #3b006f;
    --ring-grey: #c8c8c8;
    --white: #ffffff;
    --band-blue: #5281f9;
    --ink: #2b2b33;
    --brand-grey: #858585;
    --photo-light: #d9d9d9;
    --photo-dark: #3a3a3a;
  }
  html, body {
    margin: 0;
    padding: 0;
    width: 1200px;
    height: 1200px;
    overflow: hidden;
    background: var(--purple);
  }
  .poster {
    position: relative;
    width: 1200px;
    height: 1200px;
    overflow: hidden;
    font-family: "Poppins", sans-serif;
  }
  .backdrop, .portrait {
    position: absolute;
    left: 0;
    top: 0;
  }
  .brand {
    position: absolute;
    right: 48px;
    top: 178px;
    display: flex;
    align-items: center;
    gap: 16px;
    font-weight: 400;
    font-size: 58px;
    line-height: 1;
    color: var(--brand-grey);
    letter-spacing: 0.5px;
  }
  .brand-mark {
    width: 34px;
    height: 34px;
    background: var(--band-blue);
  }
  .tour-title {
    position: absolute;
    left: 230px;
    top: 282px;
    margin: 0;
    font-weight: 700;
    font-size: 56px;
    line-height: 72px;
    letter-spacing: -1px;
    color: var(--ink);
  }
  .tour-title .headline {
    display: block;
    color: var(--white);
  }
  .tour-title .line { display: block; }
</style>
</head>
<body>
<main class="poster">
  <svg class="backdrop" width="1200" height="1200" viewBox="0 0 1200 1200" aria-hidden="true">
    <defs>
      <clipPath id="inner-circle">
        <ellipse cx="920" cy="520" rx="774" ry="722"/>
      </clipPath>
    </defs>
    <rect width="1200" height="1200" fill="var(--purple)"/>
    <ellipse class="ring" cx="920" cy="520" rx="874" ry="802" fill="var(--ring-grey)"/>
    <ellipse class="inner" cx="920" cy="520" rx="774" ry="722" fill="var(--white)"/>
    <rect class="title-band" x="0" y="250" width="1200" height="250" fill="var(--band-blue)" clip-path="url(#inner-circle)"/>
  </svg>

  <div class="brand">
    <span class="brand-mark"></span>
    <span class="brand-name">dan hollis</span>
  </div>

  <h1 class="tour-title">
    <span class="line">The</span>
    <span class="headline">Bright Window</span>
    <span class="line">Tour 2019</span>
  </h1>

  <svg class="portrait" width="1200" height="1200" viewBox="0 0 1200 1200" role="img" aria-label="Black and white head-and-shoulders photo of the speaker, a short-haired man in a dark V-neck shirt">
    <defs>
      <linearGradient id="photo-tone" x1="0" y1="0" x2="0" y2="1">
        <stop offset="0" stop-color="var(--photo-dark)"/>
        <stop offset="0.12" stop-color="var(--photo-light)"/>
        <stop offset="0.7" stop-color="#bdbdbd"/>
        <stop offset="0.85" stop-color="var(--photo-dark)"/>
        <stop offset="1" stop-color="#1f1f1f"/>
      </linearGradient>
    </defs>
    <path fill="url(#photo-tone)" d="M880 332 C1000 330 1090 400 1105 520 L1120 600 C1135 640 1120 720 1095 760 C1090 860 1110 930 1200 980 L1200 1200 L580 1200 C640 1120 760 1070 810 1000 C775 940 750 860 740 790 C700 760 665 700 668 620 C672 580 690 570 700 580 C700 440 760 340 880 332 Z"/>
  </svg>
</main>
</body>
</html>
```